IT Company seeking creative modern BUSINESS CARD DESIGN!

We are a full service IT company located in California. We specialize in offering computer network support to small to medium to enterprise sized businesses. We are looking for a new business card design to go with our newly designed logo. We prefer business cards that are unique and make a lasting impression. We tend to like business cards with black, gray or blue backgrounds. Our color theme should include black, blue, gray and white only. We want something BOLD, BRIGHT, FUN, CLEAN, and MODERN. Please design with creativity in mind! :) We want our business cards to "pop" and "stand out" when compared to other business cards side by side. We want to be different and make that WINNING first impression every time!! =)

FONT NAME FOR harbor forgeworks is "Cynthe" True Type font.

BLUE LOGO COLOR IS:
Hex: #2375BB
R: 35
G: 117
B: 187

The secondary color is pure "Black". Use of Grayscale is okay too.
Updates

Please look over the sample designs I attached. ** IMPORTANT ** This will give you an idea of the color, design and layouts we like. Also, our logo needs to stand out (nothing small and DO NOT duplicate logo twice on same side of the card. We do want a front and back to the card design. You are welcome to separate the circle logo and the business name if needed. Also, please no pastel colors or busy backgrounds with design. Watermark backgrounds would be okay if it works with the logo design. Let me know if you have any issues opening the logo or font file. Thanks a bunch! EXCITED and AWAITING your designs! I will provide as much feedback as possible. Thank you, Lorna :)

Target Market(s)

Small, Medium to Enterprise businesses. Business Card will be given to professionals. We want the card to stand out and look and feel different.

Industry/Entity Type

Computer

Font styles to use
Sans Serif

Colors
0555a3
ffffff
000000
474747
959595
5c5c5c
c8c8c8
eeeeee
3276b5

Requirements
Must have
• WE WANT TO STAND OUT! BE DIFFERENT! MAKE A LASTING IMPRESSION!

We like clean, neat, modern, BOLD look. See attachment for samples of designs we like.

This is the information needed on the business card. Exact information will change per employee (of course), but heres the required data needed (this info can go on either the front or back of the business card).

Business Logo (File attached)

Gavin Trelawny
CEO / Senior Network Engineer
7190 Dalworth Avenue
Suite F
Brenfield, CA 95872

main tel: 209-555-0147
direct tel: 209-555-0182
cell: 209-555-0163
fax tel: 209-xxx-xxxx

gtrelawny@hfgw.example
www.hfgw.example

We really like the use of icons for the address, phone, location etc. Looks modern and clean.

Nice to have
• Somewhere it would be nice to include the cities we are located in and serving:
Brenfield - Varlow - Ostmere - Kestrelton (FYI - if there's no design space to include these cities, then that's okay. This is just a wish list item to include if theres room. =)

We like watermark background effects if that's an option. Not necessary though.

If there's a way to include we are on Chatterloop, Workmesh, and Chirpline - that would be cool, but not necessary.

Different Card Size or cut ot rounded edges might be cool, but not necessary. We do want to STAND OUT and be different.
Should not have
• No other colors other than Blue, Black, Gray, White. Do not like pastel blue or light blue. For lighter coloring.... would prefer gray scale or white. Keep BLUE color bold and vibrant (like samples I attached).

Do not do a traditional white business card. Too boring and ordinary. Do not make address and phone information in large fat fonts. We want neat and tidy - modern looking fonts. :)

```html
<!DOCTYPE html>
<html lang="en">
<head>
<meta charset="utf-8">
<title>harbor forgeworks – business cards</title>
<link rel="stylesheet" href="https://fonts.googleapis.com/css2?family=Roboto:wght@400;500;700&display=swap">
<style>
:root{
  --blue:#2f7bc4;
  --blue-bright:#2a80d6;
  --blue-back:#3a7cc0;
  --ink:#232323;
  --row:#2b2b2b;
  --rule:#6e6e6e;
  --white:#ffffff;
  --page:#ffffff;
}
*{margin:0;padding:0;box-sizing:border-box}
html,body{width:1200px;height:2357px;overflow:hidden;background:var(--page);font-family:"Roboto",Arial,sans-serif}
.canvas{position:relative;width:1200px;height:2357px}
.card{position:absolute;overflow:hidden;border:2px solid #1a1a1a}
.abs{position:absolute}
.accent{color:var(--blue-bright)}
.brand{font-family:"Roboto",Arial,sans-serif;font-weight:500;color:var(--blue-bright);white-space:nowrap;letter-spacing:1px}
.icon{fill:var(--white)}

/* vertical front */
.v-front{left:46px;top:36px;width:556px;height:952px;background:var(--white)}
.v-front .tab{left:0;top:0}
.v-front .mark{left:222px;top:140px;width:112px;height:112px;border-radius:50%;background:var(--blue)}
.v-front .brand{left:0;width:100%;top:282px;text-align:center;font-size:42px}
.info-row{position:absolute;left:0;width:100%;color:var(--white)}
.info-row .ico{position:absolute;left:40px;width:40px;height:40px}
.info-row .txt{position:absolute;left:144px;font-size:20px;line-height:25px}
.info-row .dash{position:absolute;right:34px;width:20px;height:5px;background:var(--blue-bright)}
.row-name{top:478px;height:116px;background:var(--blue)}
.row-name .person{font-weight:700;font-size:30px;line-height:36px}
.row-name .role{font-weight:700;font-size:19px;line-height:26px}
.row-name .dash{background:var(--white);top:56px}
.row-dark{background:var(--row);border-top:1px solid var(--rule)}
.row-phone{top:594px;height:120px}
.row-web{top:714px;height:120px}
.row-addr{top:834px;height:118px}

/* vertical back */
.v-back{left:620px;top:36px;width:558px;height:952px;background:var(--blue-back)}
.v-back .disc{left:152px;top:266px;width:256px;height:256px;border-radius:50%;background:var(--white);display:flex;align-items:center;justify-content:center;text-align:center}
.v-back .brand{font-size:34px;line-height:42px;color:var(--blue-back)}
.cities{font-weight:700;color:var(--white);white-space:nowrap}
.cities i{font-style:normal;color:var(--blue-bright);padding:0 4px}
.v-back .strip{left:0;top:834px;width:100%;height:118px;background:var(--row);display:flex;align-items:center;justify-content:center;font-size:21px}

/* horizontal front */
.h-front{left:46px;top:1026px;width:1132px;height:662px;background:var(--ink)}
.h-front .band{left:0;top:184px;width:100%;height:164px;background:var(--blue-bright)}
.h-front .halo{left:418px;top:130px;width:272px;height:272px;border-radius:50%;background:var(--ink)}
.h-front .mark{left:458px;top:170px;width:192px;height:192px;border-radius:50%;background:var(--blue-bright);border:6px solid var(--white)}
.h-front .brand{left:0;width:100%;top:410px;text-align:center;font-size:64px}

/* horizontal back */
.h-back{left:46px;top:1700px;width:1132px;height:640px;background:var(--ink);color:var(--white)}
.h-back .ribbon{left:76px;top:0;width:150px;height:100%;background:var(--blue-bright)}
.h-back .mark{left:90px;top:37px;width:122px;height:122px;border-radius:50%;border:6px solid var(--white);background:var(--blue-bright)}
.h-back .pill{left:68px;top:180px;width:166px;height:410px;border-radius:83px;background:var(--ink)}
.h-back .nameplate{left:151px;top:385px;transform:translate(-50%,-50%) rotate(-90deg);white-space:nowrap;text-align:center}
.h-back .nameplate .person{font-weight:700;font-size:34px;line-height:40px}
.h-back .nameplate .role{font-size:24px;line-height:30px}
.h-back .brand{left:294px;top:30px;font-size:58px}
.h-back .addr{left:484px;width:400px;top:278px;text-align:center;font-size:24px;line-height:30px}
.h-back .timeline{left:0;top:0}
.h-back .phones{left:238px;width:400px;top:458px;text-align:center;font-size:24px;line-height:30px}
.h-back .web{left:746px;width:400px;top:458px;text-align:center;font-size:24px;line-height:30px}
.h-back .cities{left:0;width:100%;top:596px;text-align:center;font-size:24px;padding-left:260px}
</style>
</head>
<body>
<svg width="0" height="0" style="position:absolute">
  <defs>
    <symbol id="i-person" viewBox="0 0 40 40"><circle cx="20" cy="12" r="8"/><path d="M6 38c0-9 6-14 14-14s14 5 14 14z"/></symbol>
    <symbol id="i-phone" viewBox="0 0 40 40"><path d="M4 14c0-5 7-8 16-8s16 3 16 8v3h-8v-4c-2-1-5-1-8-1s-6 0-8 1v4H4z"/><path d="M10 20l4-4h12l4 4v14H10z"/><g fill="#2b2b2b"><rect x="14" y="22" width="3" height="3"/><rect x="19" y="22" width="3" height="3"/><rect x="24" y="22" width="3" height="3"/><rect x="14" y="27" width="3" height="3"/><rect x="19" y="27" width="3" height="3"/><rect x="24" y="27" width="3" height="3"/></g></symbol>
    <symbol id="i-globe" viewBox="0 0 40 40"><circle cx="20" cy="20" r="16" fill="none" stroke="#fff" stroke-width="3"/><ellipse cx="20" cy="20" rx="7" ry="16" fill="none" stroke="#fff" stroke-width="2.5"/><path d="M4 20h32M7 12h26M7 28h26" stroke="#fff" stroke-width="2.5"/></symbol>
    <symbol id="i-home" viewBox="0 0 40 40"><path d="M20 4l18 16h-5v16H24V26h-8v10H7V20H2z"/><rect x="28" y="6" width="5" height="9"/></symbol>
  </defs>
</svg>

<main class="canvas">

  <section class="card v-front">
    <svg class="abs tab" width="556" height="40"><polygon points="124,0 432,0 392,38 164,38" fill="var(--blue)"/></svg>
    <div class="abs mark"></div>
    <div class="abs brand">harbor forgeworks</div>

    <div class="info-row row-name">
      <svg class="ico icon" style="top:38px"><use href="#i-person"/></svg>
      <div class="txt" style="top:20px"><div class="person">GAVIN TRELAWNY</div><div class="role">President / CEO</div></div>
      <div class="dash"></div>
    </div>
    <div class="info-row row-dark row-phone">
      <svg class="ico icon" style="top:40px"><use href="#i-phone"/></svg>
      <div class="txt" style="top:22px">209.555.0147 <span class="accent">Help Desk</span><br>209.555.0182 <span class="accent">Direct</span><br>209.555.0163 <span class="accent">Cell</span></div>
      <div class="dash" style="top:57px"></div>
    </div>
    <div class="info-row row-dark row-web">
      <svg class="ico icon" style="top:40px"><use href="#i-globe"/></svg>
      <div class="txt" style="top:34px">gtrelawny@hfgw.example<br>www.hfgw.example</div>
      <div class="dash" style="top:57px"></div>
    </div>
    <div class="info-row row-dark row-addr">
      <svg class="ico icon" style="top:40px"><use href="#i-home"/></svg>
      <div class="txt" style="top:32px">7190 Dalworth Avenue, Suite F<br>Brenfield, CA 95872</div>
      <div class="dash" style="top:57px"></div>
    </div>
  </section>

  <section class="card v-back">
    <div class="abs disc"><div class="brand">harbor<br>forgeworks</div></div>
    <div class="abs strip cities">Brenfield <i>●</i> Ostmere <i>●</i> Varlow <i>●</i> Kestrelton</div>
  </section>

  <section class="card h-front">
    <div class="abs band"></div>
    <div class="abs halo"></div>
    <div class="abs mark"></div>
    <div class="abs brand">harbor forgeworks</div>
  </section>

  <section class="card h-back">
    <div class="abs ribbon"></div>
    <div class="abs mark"></div>
    <div class="abs pill"></div>
    <div class="abs nameplate"><div class="person">Gavin Trelawny</div><div class="role">President / CEO</div></div>
    <div class="abs brand">harbor forgeworks</div>
    <div class="abs addr">7190 Dalworth Avenue, Suite F<br>Brenfield, CA 95872</div>
    <svg class="abs timeline" width="1132" height="460">
      <line x1="338" y1="400" x2="1038" y2="400" stroke="var(--blue-bright)" stroke-width="3"/>
      <g stroke="var(--blue-bright)" stroke-width="3">
        <line x1="438" y1="362" x2="438" y2="438"/><line x1="686" y1="362" x2="686" y2="438"/><line x1="946" y1="362" x2="946" y2="438"/>
      </g>
      <g fill="var(--blue-bright)"><circle cx="438" cy="400" r="28"/><circle cx="686" cy="400" r="28"/><circle cx="946" cy="400" r="28"/></g>
      <g class="icon">
        <use href="#i-phone" x="424" y="386" width="28" height="28"/>
        <use href="#i-home" x="672" y="386" width="28" height="28"/>
        <use href="#i-globe" x="932" y="386" width="28" height="28"/>
      </g>
    </svg>
    <div class="abs phones">209.555.0147 <span class="accent">Help Desk</span><br>209.555.0182 <span class="accent">Direct</span><br>209.555.0163 <span class="accent">Cell</span></div>
    <div class="abs web">gtrelawny@hfgw.example<br>www.hfgw.example</div>
    <div class="abs cities">Brenfield <i>●</i> Ostmere <i>●</i> Varlow <i>●</i> Kestrelton</div>
  </section>

</main>
</body>
</html>
```